Webdesign für K&L Vendora GmbH
Zielgruppe
- Partner für moderne Automaten- und Verpflegungslösungen in Unternehmen
- Zielgruppe sind Unternehmen, welche Versorgungskonzepte schaffen, die optimal auf die Bedürfnisse von Mitarbeitenden, Kunden und Gästen abgestimmt sind
Aufgabenstellung
- KEINE Kopie der alten Webseite
- Farbkonzept gern in sanften Kaffeetönen kombiniert mit Weiß
- Klare Struktur der Webseite

```html
<!DOCTYPE html>
<html lang="de">
<head>
<meta charset="utf-8">
<title>K&amp;L Vendora GmbH – Webdesign</title>
<link href="https://fonts.googleapis.com/css2?family=Inter:wght@400;500;600;700;800;900&display=swap" rel="stylesheet">
<style>
:root{
  --espresso:#3b2417;
  --mocha:#6b4a33;
  --latte:#b08a68;
  --cream:#f3ebe1;
  --ink:#1f1a17;
  --field:#f6f1eb;
  --white:#ffffff;
}
*{box-sizing:border-box;margin:0;padding:0}
html,body{width:1200px;height:1200px;overflow:hidden;background:var(--white);font-family:"Inter",sans-serif;color:var(--ink)}
.board{position:relative;width:1200px;height:1200px;overflow:hidden}

.brand-block{position:absolute;left:775px;top:73px;display:flex;align-items:center;gap:22px}
.brand-block .dot{width:116px;height:116px;border-radius:50%;background:var(--cream)}
.brand-block .name{font-weight:800;font-size:40px;line-height:1.1;color:var(--ink)}

.page{position:absolute;width:653px;height:1785px;background:var(--white);box-shadow:0 6px 28px rgba(0,0,0,.16);overflow:hidden;transform-origin:0 0}
.page--overview{left:37.5px;top:36px;transform:scale(.637)}
.page--detail{left:503px;top:242px}
.abs{position:absolute}

.logo-dot{left:38px;top:8px;width:36px;height:36px;border-radius:50%;background:var(--cream)}
.logo-name{left:81px;top:19px;font-weight:700;font-size:10.5px;color:var(--ink)}
.nav{top:19px;font-size:9px;font-weight:600;color:var(--ink)}
.nav.active{text-decoration:underline;text-decoration-color:var(--latte);text-underline-offset:3px}
.burger{left:630px;top:21px;width:9px}
.burger i{display:block;height:1.4px;background:var(--ink);margin-bottom:2px}
.contact-pill{left:502px;top:38px;width:151px;height:13px;background:var(--latte);border-radius:7px 0 0 7px;color:#fff;font-size:6.3px;font-weight:500;display:flex;align-items:center;justify-content:space-around;padding-left:4px}

.hero-photo{left:0;top:51px;width:653px;height:316px;background:linear-gradient(100deg,#f1ebe2 0%,#e1d3c1 38%,#b99a7c 62%,#4a3a30 86%,#2c2320 100%)}
.hero-dot{left:31px;top:95px;width:28px;height:28px;border-radius:50%;background:#fff;color:var(--espresso);font-size:7px;font-weight:800;display:flex;align-items:center;justify-content:center}
.hero-title{left:31px;top:135px;font-size:20.5px;font-weight:900;line-height:1.08;color:var(--ink)}
.hero-sub{left:31px;top:191px;font-size:12.5px;line-height:1.2;color:var(--ink)}
.hero-text{left:31px;top:231px;width:200px;font-size:7.4px;line-height:1.4;color:var(--ink)}
.btn{background:var(--espresso);color:#fff;border-radius:14px;font-weight:600;display:flex;align-items:center;justify-content:center}
.hero-btn{left:32px;top:288px;width:81px;height:26px;font-size:9px}
.call-badge{left:228px;top:268px;width:76px;height:76px;border-radius:50%;background:var(--latte);color:#fff;font-size:7.4px;line-height:1.2;text-align:center;display:flex;align-items:center;justify-content:center;transform:rotate(14deg)}

.concept-circle{left:44px;top:397px;width:248px;height:248px;border-radius:50%;background:var(--latte)}
.machine-a{left:64px;top:413px;width:106px;height:206px;background:linear-gradient(180deg,#2a2a2c,#7a2d22 30%,#c2892e 55%,#1f1f22 80%,#cfcfd2);border-radius:3px}
.machine-b{left:184px;top:436px;width:84px;height:225px;background:linear-gradient(180deg,#3a2a20,#1c1c1e 25%,#4b3a28 40%,#1c1c1e 60%,#5a3a24 80%,#2a1c14);border-radius:3px}
.heading{font-weight:800;color:var(--espresso);line-height:1.12}
.rule{width:21px;height:2px;background:var(--latte)}
.concept-title{left:336px;top:418px;font-size:20.5px}
.concept-rule{left:337px;top:470px}
.concept-lead{left:336px;top:493px;width:300px;font-size:8.6px;line-height:1.45}
.concept-label{left:336px;top:557px;font-size:8.4px;font-weight:700}
.checks{list-style:none;font-size:8.6px;line-height:13.4px}
.checks li::before{content:"✓";color:var(--latte);font-weight:700;margin-right:5px;font-size:7.5px}
.concept-list{left:336px;top:580px;width:310px}

.card{top:700px;width:104px;height:152px;background:#fff;border-radius:9px;box-shadow:0 2px 9px rgba(0,0,0,.12);text-align:center}
.card svg{position:absolute;left:30px;top:17px;width:44px;height:62px;color:var(--espresso)}
.card-title{position:absolute;left:0;right:0;top:90px;font-size:9.3px;font-weight:700;color:var(--espresso);line-height:1.15}
.card-text{position:absolute;left:6px;right:6px;top:117px;font-size:6.7px;line-height:1.18;color:var(--mocha)}

.hand-title{left:45px;top:910px;font-size:20.5px}
.hand-rule{left:45px;top:943px}
.hand-lead{left:45px;top:978px;width:280px;font-size:8.4px;line-height:1.4}
.hand-list{left:45px;top:1045px;font-size:8.2px;line-height:13.5px}
.hand-photo{left:363px;top:897px;width:290px;height:231px;background:linear-gradient(110deg,#e2d8ca 0%,#8d6a4c 35%,#2e2724 65%,#1e1a18 100%)}
.hand-dot{left:329px;top:1045px;width:60px;height:60px;border-radius:50%;background:#fff;box-shadow:0 2px 8px rgba(0,0,0,.2);color:var(--espresso);font-weight:800;font-size:11px;display:flex;align-items:center;justify-content:center}

.why{left:0;top:1158px;width:653px;height:139px;background:var(--latte);color:#fff;text-align:center}
.why h3{margin-top:23px;font-size:16px;font-weight:700}
.why p{margin:16px auto 0;width:470px;font-size:8.3px;line-height:1.6}

.inquiry-title{left:45px;top:1330px;font-size:20.5px}
.inquiry-rule{left:45px;top:1360px}
.inquiry-lead{left:45px;top:1386px;font-size:8.6px;line-height:1.55}
.field{background:var(--field);font-size:8.4px;font-weight:500;padding:8px 11px}
.map{left:497px;top:1440px;width:110px;height:173px;border-radius:6px;background:linear-gradient(160deg,#f2eee8,#e6ddd1 50%,#efe9df)}
.send-btn{left:46px;top:1638px;width:81px;height:25px;font-size:8.4px}

.footer{left:0;top:1688px;width:653px;height:97px;background:var(--espresso);color:#fff;font-size:8px;line-height:1.5}
.f-dot{left:37px;top:28px;width:42px;height:42px;border-radius:50%;background:#fff;color:var(--espresso);font-size:8px;font-weight:800;display:flex;align-items:center;justify-content:center}
</style>
</head>
<body>
<div class="board">

  <div class="brand-block">
    <div class="dot"></div>
    <div class="name">K&amp;L Vendora<br>GmbH</div>
  </div>

  <section class="page page--overview">
    <div class="abs logo-dot"></div>
    <div class="abs logo-name">K&amp;L Vendora GmbH</div>
    <span class="abs nav active" style="left:292px">Home</span>
    <span class="abs nav" style="left:369px">Produkte</span>
    <span class="abs nav" style="left:448px">Über Uns</span>
    <span class="abs nav" style="left:528px">Kontakt</span>
    <div class="abs burger"><i></i><i></i><i></i></div>
    <div class="abs contact-pill"><span>+49 371 555019</span><span>info@kl-vendora.de</span></div>

    <div class="abs hero-photo" role="img" aria-label="Foto: lächelnde Frau bedient einen Snackautomaten im Büro"></div>
    <div class="abs hero-dot">K&amp;L</div>
    <h1 class="abs hero-title">MODERNE AUTOMATEN<br>FÜR UNTERNEHMEN</h1>
    <p class="abs hero-sub">Kaffee, Getränke und Snacks<br>mit Rundum-Service</p>
    <p class="abs hero-text">Wir treffen mit Ihnen eine bedarfsgerechte Auswahl an Heißgetränkeautomaten, Kaltgetränkeautomaten, Snack- und Speiseautomaten, sowie für Wasserspender in verschiednen Varianten.</p>
    <div class="abs btn hero-btn">Mehr erfahren</div>
    <div class="abs call-badge"><span>Rufen Sie uns<br>an unter:<br><b>+49 371 555019</b></span></div>

    <div class="abs concept-circle"></div>
    <div class="abs machine-a" role="img" aria-label="Foto: Snackautomat"></div>
    <div class="abs machine-b" role="img" aria-label="Foto: Kaffeeautomat"></div>
    <h2 class="abs heading concept-title">Maßgeschneiderte<br>Versorgungskonzepte</h2>
    <div class="abs rule concept-rule"></div>
    <p class="abs concept-lead">Jedes Unternehmen hat unterschiedliche Bedürfnisse.<br>Deshalb beraten wir Sie persönlich und entwickeln gemeinsam<br>mit Ihnen die optimale Lösung für Ihren Standort.</p>
    <p class="abs concept-label">Unser Angebot umfasst:</p>
    <ul class="abs checks concept-list">
      <li>Heißgetränkeautomaten für Kaffee, Cappuccino,</li>
      <li>Kakao und weitere Spezialitäten</li>
      <li>Kaltgetränkeautomaten für Erfrischungsgetränke und Wasser</li>
      <li>Snack- und Speiseautomaten für die Verpflegung rund um die Uhr</li>
      <li>Wasserspender für Büros, Produktionsstätten und Empfangsbereiche</li>
      <li>Moderne Bezahlsysteme und individuelle Ausstattungsoptionen</li>
    </ul>

    <div class="abs card" style="left:37px"><svg viewBox="0 0 44 62" fill="none" stroke="currentColor" stroke-width="1.6"><rect x="2" y="2" width="40" height="58" rx="2"/><rect x="7" y="7" width="20" height="30"/><line x1="31" y1="2" x2="31" y2="60"/><rect x="9" y="45" width="16" height="8"/><circle cx="36" cy="12" r="1.5"/><circle cx="36" cy="20" r="1.5"/><circle cx="36" cy="28" r="1.5"/></svg><div class="card-title">Standgeräte</div><div class="card-text">flexible Lösungen<br>für verschiedene<br>Einsatzbereiche</div></div>
    <div class="abs card" style="left:156px"><svg viewBox="0 0 44 62" fill="none" stroke="currentColor" stroke-width="1.6"><rect x="2" y="2" width="40" height="58" rx="2"/><rect x="7" y="7" width="20" height="30"/><line x1="31" y1="2" x2="31" y2="60"/><path d="M11 20h11v8a5 5 0 0 1-11 0z"/><rect x="9" y="45" width="16" height="8"/><circle cx="36" cy="12" r="1.5"/><circle cx="36" cy="20" r="1.5"/></svg><div class="card-title">InCup-Systeme</div><div class="card-text">schnelle, saubere und<br>praktische<br>Getränkezubereitung</div></div>
    <div class="abs card" style="left:275px"><svg viewBox="0 0 44 62" fill="none" stroke="currentColor" stroke-width="1.6"><rect x="2" y="2" width="40" height="58" rx="2"/><rect x="7" y="7" width="20" height="30"/><line x1="31" y1="2" x2="31" y2="60"/><rect x="11" y="17" width="6" height="15" rx="2"/><rect x="9" y="45" width="16" height="8"/><circle cx="36" cy="12" r="1.5"/><circle cx="36" cy="20" r="1.5"/></svg><div class="card-title" style="top:84px">Kaltgetränke<br>Automaten</div><div class="card-text">gekühlte Erfrischungen<br>jederzeit verfügbar</div></div>
    <div class="abs card" style="left:394px"><svg viewBox="0 0 44 62" fill="none" stroke="currentColor" stroke-width="1.6"><rect x="2" y="2" width="40" height="58" rx="2"/><rect x="7" y="7" width="20" height="30"/><line x1="31" y1="2" x2="31" y2="60"/><line x1="7" y1="22" x2="27" y2="22"/><rect x="9" y="45" width="16" height="8"/><circle cx="36" cy="12" r="1.5"/><circle cx="36" cy="20" r="1.5"/></svg><div class="card-title" style="top:84px">Snack<br>Automaten</div><div class="card-text">schnelle Verpflegung<br>für zwischendurch</div></div>
    <div class="abs card" style="left:513px"><svg viewBox="0 0 44 62" fill="none" stroke="currentColor" stroke-width="1.6"><rect x="14" y="2" width="16" height="14" rx="2"/><rect x="10" y="18" width="24" height="42" rx="2"/><rect x="16" y="34" width="12" height="10"/></svg><div class="card-title" style="top:96px">Wasserspender</div><div class="card-text">frisches Trinkwasser<br>für Büro &amp; Betrieb</div></div>

    <h2 class="abs heading hand-title">Alles aus einer Hand</h2>
    <div class="abs rule hand-rule"></div>
    <p class="abs hand-lead">Von der persönlichen Beratung über die Installation bis hin zur regelmäßigen Wartung und Befüllung Ihrer Automaten kümmern wir uns um den kompletten Betrieb.</p>
    <ul class="abs checks hand-list">
      <li>Individuelle Beratung vor Ort</li>
      <li>Zuverlässiger Kundenservice in Sachsen</li>
      <li>Moderne, leistungsstarke Geräte</li>
      <li>Flexible und wirtschaftliche Konzepte</li>
    </ul>
    <div class="abs hand-photo" role="img" aria-label="Foto: Hand wählt Produkt am Automaten-Tastenfeld"></div>
    <div class="abs hand-dot">K&amp;L</div>

    <div class="abs why">
      <h3>Warum K&amp;L Vendora?</h3>
      <p>Als regionaler Anbieter stehen wir für Qualität, Zuverlässigkeit und persönlichen Service. Unsere Lösungen sorgen für zufriedene Mitarbeitende und einen professionellen Eindruck bei Ihren Kunden. Entscheiden Sie sich für Getränke- und Snackautomaten in Chemnitz – mit einem Partner, der Ihre Anforderungen versteht.</p>
    </div>

    <h2 class="abs heading inquiry-title">Wir freuen uns auf Ihre Anfrage</h2>
    <div class="abs rule inquiry-rule"></div>
    <p class="abs inquiry-lead">Sie möchten die Verpflegung in Ihrem Unternehmen verbessern?<br><b>Gemeinsam finden wir das passende Konzept für Ihren Bedarf.</b></p>
    <div class="abs field" style="left:45px;top:1440px;width:210px;height:27px">Name</div>
    <div class="abs field" style="left:271px;top:1440px;width:210px;height:27px">Vorname</div>
    <div class="abs field" style="left:45px;top:1477px;width:210px;height:27px">E-Mail</div>
    <div class="abs field" style="left:271px;top:1477px;width:210px;height:27px">Telefon</div>
    <div class="abs field" style="left:45px;top:1513px;width:436px;height:100px">Nachricht</div>
    <div class="abs map" role="img" aria-label="Karte mit Standortmarkierung"></div>
    <div class="abs btn send-btn">Absenden</div>

    <footer class="abs footer">
      <div class="abs f-dot">K&amp;L</div>
      <div class="abs" style="left:128px;top:30px">K&amp;L Vendora GmbH<br>Am Lindenhof 12<br>09120 Chemnitz</div>
      <div class="abs" style="left:263px;top:42px">Tel.&nbsp;&nbsp;&nbsp;&nbsp;0371-555020<br>Fax.&nbsp;&nbsp;&nbsp;0371 555021</div>
      <div class="abs" style="left:372px;top:54px">kontakt@kl-vendora.de</div>
      <div class="abs" style="left:565px;top:54px;opacity:.8">Impressum</div>
    </footer>
  </section>

  <section class="page page--detail">
    <div class="abs logo-dot"></div>
    <div class="abs logo-name">K&amp;L Vendora GmbH</div>
    <span class="abs nav active" style="left:292px">Home</span>
    <span class="abs nav" style="left:369px">Produkte</span>
    <span class="abs nav" style="left:448px">Über Uns</span>
    <span class="abs nav" style="left:528px">Kontakt</span>
    <div class="abs burger"><i></i><i></i><i></i></div>
    <div class="abs contact-pill"><span>+49 371 555019</span><span>info@kl-vendora.de</span></div>

    <div class="abs hero-photo" role="img" aria-label="Foto: lächelnde Frau bedient einen Snackautomaten im Büro"></div>
    <div class="abs hero-dot">K&amp;L</div>
    <h1 class="abs hero-title">MODERNE AUTOMATEN<br>FÜR UNTERNEHMEN</h1>
    <p class="abs hero-sub">Kaffee, Getränke und Snacks<br>mit Rundum-Service</p>
    <p class="abs hero-text">Wir treffen mit Ihnen eine bedarfsgerechte Auswahl an Heißgetränkeautomaten, Kaltgetränkeautomaten, Snack- und Speiseautomaten, sowie für Wasserspender in verschiednen Varianten.</p>
    <div class="abs btn hero-btn">Mehr erfahren</div>
    <div class="abs call-badge"><span>Rufen Sie uns<br>an unter:<br><b>+49 371 555019</b></span></div>

    <div class="abs concept-circle"></div>
    <div class="abs machine-a" role="img" aria-label="Foto: Snackautomat"></div>
    <div class="abs machine-b" role="img" aria-label="Foto: Kaffeeautomat"></div>
    <h2 class="abs heading concept-title">Maßgeschneiderte<br>Versorgungskonzepte</h2>
    <div class="abs rule concept-rule"></div>
    <p class="abs concept-lead">Jedes Unternehmen hat unterschiedliche Bedürfnisse.<br>Deshalb beraten wir Sie persönlich und entwickeln gemeinsam<br>mit Ihnen die optimale Lösung für Ihren Standort.</p>
    <p class="abs concept-label">Unser Angebot umfasst:</p>
    <ul class="abs checks concept-list">
      <li>Heißgetränkeautomaten für Kaffee, Cappuccino,</li>
      <li>Kakao und weitere Spezialitäten</li>
      <li>Kaltgetränkeautomaten für Erfrischungsgetränke und Wasser</li>
      <li>Snack- und Speiseautomaten für die Verpflegung rund um die Uhr</li>
      <li>Wasserspender für Büros, Produktionsstätten und Empfangsbereiche</li>
      <li>Moderne Bezahlsysteme und individuelle Ausstattungsoptionen</li>
    </ul>

    <div class="abs card" style="left:37px"><svg viewBox="0 0 44 62" fill="none" stroke="currentColor" stroke-width="1.6"><rect x="2" y="2" width="40" height="58" rx="2"/><rect x="7" y="7" width="20" height="30"/><line x1="31" y1="2" x2="31" y2="60"/><rect x="9" y="45" width="16" height="8"/><circle cx="36" cy="12" r="1.5"/><circle cx="36" cy="20" r="1.5"/><circle cx="36" cy="28" r="1.5"/></svg><div class="card-title">Standgeräte</div><div class="card-text">flexible Lösungen<br>für verschiedene<br>Einsatzbereiche</div></div>
    <div class="abs card" style="left:156px"><svg viewBox="0 0 44 62" fill="none" stroke="currentColor" stroke-width="1.6"><rect x="2" y="2" width="40" height="58" rx="2"/><rect x="7" y="7" width="20" height="30"/><line x1="31" y1="2" x2="31" y2="60"/><path d="M11 20h11v8a5 5 0 0 1-11 0z"/><rect x="9" y="45" width="16" height="8"/><circle cx="36" cy="12" r="1.5"/><circle cx="36" cy="20" r="1.5"/></svg><div class="card-title">InCup-Systeme</div><div class="card-text">schnelle, saubere und<br>praktische<br>Getränkezubereitung</div></div>
    <div class="abs card" style="left:275px"><svg viewBox="0 0 44 62" fill="none" stroke="currentColor" stroke-width="1.6"><rect x="2" y="2" width="40" height="58" rx="2"/><rect x="7" y="7" width="20" height="30"/><line x1="31" y1="2" x2="31" y2="60"/><rect x="11" y="17" width="6" height="15" rx="2"/><rect x="9" y="45" width="16" height="8"/><circle cx="36" cy="12" r="1.5"/><circle cx="36" cy="20" r="1.5"/></svg><div class="card-title" style="top:84px">Kaltgetränke<br>Automaten</div><div class="card-text">gekühlte Erfrischungen<br>jederzeit verfügbar</div></div>
    <div class="abs card" style="left:394px"><svg viewBox="0 0 44 62" fill="none" stroke="currentColor" stroke-width="1.6"><rect x="2" y="2" width="40" height="58" rx="2"/><rect x="7" y="7" width="20" height="30"/><line x1="31" y1="2" x2="31" y2="60"/><line x1="7" y1="22" x2="27" y2="22"/><rect x="9" y="45" width="16" height="8"/><circle cx="36" cy="12" r="1.5"/><circle cx="36" cy="20" r="1.5"/></svg><div class="card-title" style="top:84px">Snack<br>Automaten</div><div class="card-text">schnelle Verpflegung<br>für zwischendurch</div></div>
    <div class="abs card" style="left:513px"><svg viewBox="0 0 44 62" fill="none" stroke="currentColor" stroke-width="1.6"><rect x="14" y="2" width="16" height="14" rx="2"/><rect x="10" y="18" width="24" height="42" rx="2"/><rect x="16" y="34" width="12" height="10"/></svg><div class="card-title" style="top:96px">Wasserspender</div><div class="card-text">frisches Trinkwasser<br>für Büro &amp; Betrieb</div></div>

    <h2 class="abs heading hand-title">Alles aus einer Hand</h2>
    <div class="abs rule hand-rule"></div>
    <div class="abs hand-photo" role="img" aria-label="Foto: Hand wählt Produkt am Automaten-Tastenfeld"></div>
  </section>

</div>
</body>
</html>
```